Need Label for Our Jams Product

HI,

we have are launching a new brand in the premium foods category by the name of Vo-Marta. the logo has been designed and our first product is Premium 65% fruit Jams. we need a label for it now. can you help ?

our flavours are strawberry, apple, mango, blackberry, cherry, PineApple.

Please note that we need one design and then we will modify it according to the flavour. so you will need to make one flavour on a theme. and then we will apply the theme accordingly to the rest of the flavours.

Target Market(s)

Health concious people who donot want to use ordinary jams any further.

Industry/Entity Type

Product

Requirements
Must have
• the logo, not too big because we need the flavour name aswell on the front of the label.
also would appreciate a touch of fruit or similar
also please note that the colour of the cap in the attached picture is the actual colour. and the label should incline with the colour of cap aswell. im not saying the label to be in that colour, but must balance the whole look of the bottle.
Please note that this is a round bottle, so much information is needed on the front. the sides of the labels will be occupied by ingredients nutrition facts etc.
Nice to have
• white background but not necessary.
Should not have
• black colour

```html
<!DOCTYPE html>
<html lang="en">
<head>
<meta charset="utf-8">
<title>Vo-Marta Strawberry Jam Label</title>
<link rel="stylesheet" href="https://fonts.googleapis.com/css2?family=Arvo:wght@400;700&family=Roboto+Slab:wght@400;600&family=Arimo:wght@400;700;800&display=swap">
<style>
  :root {
    --blush: #f7cadd;
    --berry: #a3005d;
    --berry-ink: #9b1a63;
    --stripe-pink: #dc8ab8;
    --leaf-green: #7ba43f;
    --paper: #ffffff;
    --panel-grey: #c9c9c9;
    --ink: #222222;
    --body-ink: #333333;
  }
  html, body {
    margin: 0;
    padding: 0;
    overflow: hidden;
    background: var(--paper);
  }
  .label {
    position: relative;
    width: 1200px;
    height: 257px;
    overflow: hidden;
    background: var(--paper);
    font-family: "Arimo", Arial, sans-serif;
  }
  .side-panel {
    position: absolute;
    left: 0; top: 0;
    width: 340px; height: 257px;
    background: var(--blush);
  }
  .nutrition {
    position: absolute;
    left: 56px; top: 22px;
    width: 110px; height: 216px;
  }
  .ingredients {
    position: absolute;
    left: 193px; top: 40px;
  }
  .ingredients h2 {
    margin: 0 0 7px;
    font-family: "Roboto Slab", Georgia, serif;
    font-weight: 600;
    font-size: 14px;
    line-height: 18px;
    color: var(--leaf-green);
  }
  .ingredients ul {
    list-style: none;
    margin: 0; padding: 0;
    font-family: "Arimo", Arial, sans-serif;
    font-size: 12px;
    line-height: 14px;
    letter-spacing: 0.4px;
    color: var(--body-ink);
  }
  .band-berry {
    position: absolute;
    left: 347px; top: 0;
    width: 19px; height: 257px;
    background: var(--berry);
  }
  .band-pink {
    position: absolute;
    top: 0; height: 257px;
    background: var(--stripe-pink);
  }
  .band-pink.left { left: 375px; width: 13px; }
  .band-pink.right { left: 986px; width: 14px; }
  .front {
    position: absolute;
    left: 388px; top: 0;
    width: 598px; height: 257px;
    background: var(--paper);
    overflow: hidden;
  }
  .fruit-photo {
    position: absolute;
    left: 330px; top: -10px;
    width: 300px; height: 290px;
    border-radius: 50%;
    background: radial-gradient(circle at 55% 50%, #e4e4e4 0%, #eeeeee 45%, rgba(255,255,255,0) 72%);
  }
  .brand-name {
    position: absolute;
    left: 27px; top: 12px;
    margin: 0;
    font-family: "Arimo", Arial, sans-serif;
    font-weight: 700;
    font-size: 20px;
    line-height: 24px;
    color: var(--berry-ink);
  }
  .flavour {
    position: absolute;
    left: 0; top: 0;
    width: 598px; height: 257px;
  }
  .flavour-name {
    font-family: "Arvo", "Roboto Slab", serif;
    font-weight: 700;
    fill: var(--berry-ink);
  }
  .product-type {
    font-family: "Roboto Slab", Georgia, serif;
    font-weight: 600;
    fill: var(--leaf-green);
  }
  .back-panel {
    position: absolute;
    left: 1000px; top: 0;
    width: 200px; height: 257px;
    background: var(--berry);
    overflow: hidden;
  }
  .back-ornament {
    position: absolute;
    left: 20px; top: -40px;
    width: 260px; height: 320px;
    border-radius: 50%;
    background: radial-gradient(circle at 50% 50%, rgba(255,255,255,0.06), rgba(255,255,255,0) 65%);
  }
</style>
</head>
<body>
<div class="label">

  <section class="side-panel">
    <svg class="nutrition" viewBox="0 0 110 218" preserveAspectRatio="none" aria-label="Nutrition facts">
      <rect x="0" y="0" width="110" height="218" fill="#fff"/>
      <g font-family="Arimo, Arial, sans-serif" fill="#222">
        <text x="3" y="11" font-size="12" font-weight="800">Nutrition Facts</text>
        <text x="3" y="17" font-size="4.6">Serving Size 1 cup (228g)</text>
        <text x="3" y="22" font-size="4.6">Servings Per Container 2</text>
        <rect x="3" y="24" width="104" height="4" fill="#222"/>
        <text x="3" y="33" font-size="3">Amount Per Serving</text>
        <line x1="3" y1="34.5" x2="107" y2="34.5" stroke="#222" stroke-width="0.4"/>
        <text x="3" y="40" font-size="4.6">Calories 250</text>
        <text x="50" y="40" font-size="4.6">Calories from Fat 110</text>
        <rect x="3" y="42" width="104" height="2" fill="#222"/>
        <text x="107" y="48" font-size="3.6" text-anchor="end">% Daily Value*</text>

        <rect x="3" y="50" width="104" height="26" fill="var(--panel-grey)"/>
        <text x="5" y="55" font-size="4.2">Total Fat 12g</text><text x="104" y="55" font-size="4.2" text-anchor="end">18%</text>
        <text x="9" y="61" font-size="4.2">Saturated Fat 3g</text><text x="104" y="61" font-size="4.2" text-anchor="end">15%</text>
        <text x="9" y="66" font-size="4.2" font-style="italic">Trans Fat 1.5g</text>
        <rect x="3" y="70" width="104" height="12" fill="var(--panel-grey)"/>
        <text x="5" y="75" font-size="4.2">Cholesterol 30mg</text><text x="104" y="75" font-size="4.2" text-anchor="end">10%</text>
        <text x="5" y="81" font-size="4.2">Sodium 470mg</text><text x="104" y="81" font-size="4.2" text-anchor="end">20%</text>
        <text x="5" y="87" font-size="4.2">Total Carbohydrate 31g</text><text x="104" y="87" font-size="4.2" text-anchor="end">10%</text>
        <rect x="3" y="89" width="104" height="6" fill="var(--panel-grey)"/>
        <text x="9" y="93.5" font-size="4.2">Dietary Fiber 0g</text><text x="104" y="93.5" font-size="4.2" text-anchor="end">0%</text>
        <text x="9" y="100" font-size="4.2">Sugars 5g</text>
        <text x="5" y="106" font-size="4.2">Protein 5g</text>
        <rect x="3" y="108" width="104" height="4" fill="#222"/>

        <rect x="3" y="113" width="104" height="27" fill="var(--panel-grey)"/>
        <text x="5" y="118" font-size="4.2">Vitamin A</text><text x="104" y="118" font-size="4.2" text-anchor="end">4%</text>
        <text x="5" y="124.5" font-size="4.2">Vitamin C</text><text x="104" y="124.5" font-size="4.2" text-anchor="end">2%</text>
        <text x="5" y="131" font-size="4.2">Calcium</text><text x="104" y="131" font-size="4.2" text-anchor="end">20%</text>
        <text x="5" y="137.5" font-size="4.2">Iron</text><text x="104" y="137.5" font-size="4.2" text-anchor="end">4%</text>

        <text x="5" y="146" font-size="3.2">* Percent Daily Values are based on a 2,000 calorie diet.</text>
        <text x="7" y="150" font-size="3.2">Your Daily Values may be higher or lower depending on</text>
        <text x="7" y="154" font-size="3.2">your calorie needs:</text>
        <text x="40" y="159" font-size="3.2">Calories</text><text x="62" y="159" font-size="3.2">2,000</text><text x="84" y="159" font-size="3.2">2,500</text>
        <line x1="5" y1="161" x2="105" y2="161" stroke="#222" stroke-width="0.3"/>
        <g font-size="3.2">
          <text x="5" y="166">Total Fat</text><text x="40" y="166">Less than</text><text x="62" y="166">65g</text><text x="84" y="166">80g</text>
          <text x="8" y="171">Sat Fat</text><text x="40" y="171">Less than</text><text x="62" y="171">20g</text><text x="84" y="171">25g</text>
          <text x="5" y="176">Cholesterol</text><text x="40" y="176">Less than</text><text x="62" y="176">300mg</text><text x="84" y="176">300mg</text>
          <text x="5" y="181">Sodium</text><text x="40" y="181">Less than</text><text x="62" y="181">2,400mg</text><text x="84" y="181">2,400mg</text>
          <text x="5" y="186">Total Carbohydrate</text><text x="62" y="186">300g</text><text x="84" y="186">375g</text>
          <text x="8" y="191">Dietary Fiber</text><text x="62" y="191">25g</text><text x="84" y="191">30g</text>
        </g>
      </g>
    </svg>

    <div class="ingredients">
      <h2>Ingredients</h2>
      <ul>
        <li>strawberrys</li>
        <li>sugar</li>
        <li>fruit pectin</li>
        <li>natural flavors</li>
      </ul>
    </div>
  </section>

  <div class="band-berry"></div>
  <div class="band-pink left"></div>

  <section class="front">
    <div class="fruit-photo" role="img" aria-label="Faint photograph of a strawberry behind the flavour name"></div>

    <p class="brand-name">Vo-Marta</p>

    <svg class="flavour" viewBox="0 0 598 257" aria-label="strawberry jam">
      <text class="flavour-name" x="93" y="123" font-size="124" textLength="471" lengthAdjust="spacingAndGlyphs">straw</text>
      <text class="flavour-name" x="75" y="204" font-size="120" textLength="444" lengthAdjust="spacingAndGlyphs">berry</text>
      <text class="product-type" x="0" y="0" font-size="44" transform="translate(569 222) rotate(-90)" textLength="86" lengthAdjust="spacingAndGlyphs">JAM</text>
    </svg>
  </section>

  <div class="band-pink right"></div>

  <section class="back-panel">
    <div class="back-ornament" role="img" aria-label="Faint tone-on-tone strawberry decoration"></div>
  </section>

</div>
</body>
</html>
```